training slide

We have an existing PPT template.

I am just looking for someone to make the attached slides better looking. If that goes well we have a whole bunch of presentations that need formatting in a similar style. Our customer base is made up of pharmaceutical and healthcare companies. we charge high end consultancy prices and it is very important our production value reflects this level of quality. We are not attached to the current PPT template and if anyone wants to re-visit that we would be very keen to see any ideas. We do however like our kelOrvanta logo but you can lose the energy, experience etc.

Industry/Entity Type

Training

```html
<!DOCTYPE html>
<html lang="en">
<head>
<meta charset="utf-8">
<title>kelOrvanta training slides</title>
<link href="https://fonts.googleapis.com/css2?family=Arimo:ital,wght@0,400;0,700;1,700&family=Tinos&display=swap" rel="stylesheet">
<style>
:root{
  --page:#ffffff;
  --plum-deep:#2a041e;
  --plum:#5c0b45;
  --magenta:#b80f80;
  --magenta-bright:#e8159c;
  --pink:#e6007e;
  --band:#0b0b0b;
  --white:#ffffff;
  --ink:#111111;
  --grid:#e9a9cf;
  --c-velara:#e6007e;
  --c-toriven:#6a1b8a;
  --c-sarquil:#f39200;
  --c-delvan:#c8102e;
  --c-mireta:#1a9e94;
  --c-olvex:#95c11f;
  --c-tavora:#9b1b30;
  --c-exlind:#f7b24a;
}
*{box-sizing:border-box;margin:0;padding:0}
html,body{width:1200px;height:849px;overflow:hidden;background:var(--page)}
.sheet{position:relative;width:1200px;height:849px}
.slide{
  position:absolute;width:489px;height:369px;overflow:hidden;
  background:
    radial-gradient(ellipse 70% 90% at 100% 10%, rgba(255,80,190,.55), rgba(255,80,190,0) 70%),
    radial-gradient(ellipse 60% 80% at 55% 120%, rgba(232,21,156,.35), rgba(232,21,156,0) 70%),
    linear-gradient(100deg,var(--plum-deep) 0%,var(--plum) 28%,var(--magenta) 62%,var(--magenta-bright) 100%);
}
.s4{left:90px;top:31px}
.s5{left:618px;top:31px}
.s6{left:90px;top:436px}
.s7{left:618px;top:436px}
.slide-title{
  position:absolute;left:56px;top:31px;
  font:italic 700 19px/1 "Arimo",Arial,sans-serif;color:var(--white);
}
.page-no{
  position:absolute;right:11px;top:5px;width:14px;height:13px;
  background:var(--white);color:var(--ink);
  font:700 8px/13px "Arimo",Arial,sans-serif;text-align:center;
}
.points{position:absolute;left:95px;top:93px;list-style:none}
.points li{
  font:13px/29px "Tinos","Times New Roman",serif;color:var(--white);
  display:flex;align-items:center;
}
.points svg{width:9px;height:9px;margin-right:1px}
.footer{
  position:absolute;left:0;right:0;bottom:0;height:42px;background:var(--band);
  display:flex;align-items:center;justify-content:space-between;padding:0 22px 0 32px;
}
.brand{font:700 15px/1 "Arimo",Arial,sans-serif;color:var(--pink)}
.url{font:13px/1 "Tinos","Times New Roman",serif;color:var(--white)}
.chart{position:absolute;background:var(--white);display:flex;align-items:center}
.chart-share{left:69px;top:74px;width:367px;height:194px}
.chart-volume{left:69px;top:91px;width:333px;height:194px}
.chart svg{display:block;width:100%;height:100%}
.chart text{font-family:"Arimo",Arial,sans-serif}
.line{fill:none;stroke-width:1.8;stroke-linejoin:round}
</style>
</head>
<body>
<div class="sheet">

  <section class="slide s4">
    <h2 class="slide-title">Proposition</h2>
    <div class="page-no">4</div>
    <ul class="points">
      <li><svg viewBox="0 0 10 10"><path d="M1 5.5 L4 8.5 L9 1.5" fill="none" stroke="#fff" stroke-width="1.6"/></svg>Halcyon Director Team</li>
      <li><svg viewBox="0 0 10 10"><path d="M1 5.5 L4 8.5 L9 1.5" fill="none" stroke="#fff" stroke-width="1.6"/></svg>Halcyon Academy</li>
      <li><svg viewBox="0 0 10 10"><path d="M1 5.5 L4 8.5 L9 1.5" fill="none" stroke="#fff" stroke-width="1.6"/></svg>Value Proposition Build</li>
    </ul>
    <footer class="footer"><span class="brand">kelOrvanta</span><span class="url">www.kelorvanta.co.uk</span></footer>
  </section>

  <section class="slide s5">
    <h2 class="slide-title">VP Builds</h2>
    <div class="page-no">5</div>
    <ul class="points">
      <li><svg viewBox="0 0 10 10"><path d="M1 5.5 L4 8.5 L9 1.5" fill="none" stroke="#fff" stroke-width="1.6"/></svg>Pulse Forward</li>
      <li><svg viewBox="0 0 10 10"><path d="M1 5.5 L4 8.5 L9 1.5" fill="none" stroke="#fff" stroke-width="1.6"/></svg>Outcomes Guarantee</li>
      <li><svg viewBox="0 0 10 10"><path d="M1 5.5 L4 8.5 L9 1.5" fill="none" stroke="#fff" stroke-width="1.6"/></svg>Corvexan/RADs</li>
    </ul>
    <footer class="footer"><span class="brand">kelOrvanta</span><span class="url">www.kelorvanta.co.uk</span></footer>
  </section>

  <section class="slide s6">
    <h2 class="slide-title">Chart</h2>
    <div class="page-no">6</div>
    <div class="chart chart-share">
      <svg viewBox="0 0 377 169">
        <rect x="4" y="3" width="253" height="11" fill="var(--magenta)"/>
        <text x="8" y="11" font-size="5.5" fill="#fff">NOTE – In the ARB market, Velara have exceeded 5% share of starts</text>
        <g stroke="var(--grid)" stroke-width=".5">
          <line x1="30" y1="20" x2="280" y2="20"/><line x1="30" y1="37" x2="280" y2="37"/>
          <line x1="30" y1="54" x2="280" y2="54"/><line x1="30" y1="71" x2="280" y2="71"/>
          <line x1="30" y1="89" x2="280" y2="89"/><line x1="30" y1="106" x2="280" y2="106"/>
          <line x1="30" y1="123" x2="280" y2="123"/><line x1="30" y1="140" x2="280" y2="140"/>
        </g>
        <g font-size="5" fill="#333" text-anchor="end">
          <text x="26" y="22">35.0%</text><text x="26" y="39">30.0%</text><text x="26" y="56">25.0%</text>
          <text x="26" y="73">20.0%</text><text x="26" y="91">15.0%</text><text x="26" y="108">10.0%</text>
          <text x="26" y="125">5.0%</text><text x="26" y="142">0.0%</text>
        </g>
        <g font-size="4.5" fill="#333" text-anchor="end">
          <text transform="translate(32,145) rotate(-90)">Jun-06</text><text transform="translate(57,145) rotate(-90)">Aug-06</text>
          <text transform="translate(82,145) rotate(-90)">Oct-06</text><text transform="translate(107,145) rotate(-90)">Dec-06</text>
          <text transform="translate(132,145) rotate(-90)">Feb-07</text><text transform="translate(157,145) rotate(-90)">Apr-07</text>
          <text transform="translate(182,145) rotate(-90)">Jun-07</text><text transform="translate(207,145) rotate(-90)">Aug-07</text>
          <text transform="translate(232,145) rotate(-90)">Oct-07</text><text transform="translate(257,145) rotate(-90)">Dec-07</text>
          <text transform="translate(282,145) rotate(-90)">Feb-08</text>
        </g>
        <g transform="translate(30,140) scale(12.5,-3.43)">
          <polyline class="line" vector-effect="non-scaling-stroke" stroke="var(--c-velara)" points="0,2 1,2 2,2.5 3,2 4,1.5 5,1 6,.5 7,0 8,0 9,.5 10,0 11,0 12,.5 13,1 14,1.5 15,1.5 16,2 17,3 18,3.5 19,4 20,5"/>
          <polyline class="line" vector-effect="non-scaling-stroke" stroke="var(--c-toriven)" points="0,21 1,22 2,24 3,25 4,26 5,24 6,22 7,19 8,16 9,15 10,17 11,19 12,21 13,22 14,18 15,16 16,20 17,26 18,24 19,18 20,12"/>
          <polyline class="line" vector-effect="non-scaling-stroke" stroke="var(--c-sarquil)" points="0,17 1,16 2,18 3,17 4,16 5,15 6,17 7,19 8,18 9,16 10,14 11,18 12,21 13,22 14,20 15,22 16,21 17,20 18,22 19,26 20,28"/>
          <polyline class="line" vector-effect="non-scaling-stroke" stroke="var(--c-delvan)" points="0,31 1,29 2,27 3,28 4,26 5,28 6,30 7,29 8,24 9,18 10,14 11,13 12,10 13,7 14,5 15,6 16,8 17,6 18,4 19,3 20,3"/>
          <polyline class="line" vector-effect="non-scaling-stroke" stroke="var(--c-mireta)" points="0,10 1,12 2,11 3,13 4,15 5,12 6,11 7,16 8,18 9,17 10,14 11,12 12,11 13,13 14,16 15,18 16,21 17,22 18,23 19,24 20,23"/>
          <polyline class="line" vector-effect="non-scaling-stroke" stroke="var(--c-olvex)" points="0,13 1,14 2,12 3,13 4,14 5,16 6,15 7,14 8,13 9,15 10,17 11,19 12,20 13,18 14,16 15,17 16,15 17,14 18,13 19,15 20,17"/>
        </g>
        <g font-size="5">
          <rect x="295" y="22" width="7" height="9" fill="var(--c-velara)"/><text x="306" y="29">Velara</text>
          <rect x="295" y="38" width="7" height="9" fill="var(--c-toriven)"/><text x="306" y="42">Toriven +</text><text x="306" y="48">Torivencomp</text>
          <rect x="295" y="56" width="7" height="9" fill="var(--c-sarquil)"/><text x="306" y="60">Sarquil +</text><text x="306" y="66">Cosarquil</text>
          <rect x="295" y="74" width="7" height="9" fill="var(--c-delvan)"/><text x="306" y="78">Delvan +</text><text x="306" y="84">Codelvan</text>
          <rect x="295" y="92" width="7" height="9" fill="var(--c-mireta)"/><text x="306" y="96">Mireta +</text><text x="306" y="102">MiretaPlus</text>
          <rect x="295" y="110" width="7" height="9" fill="var(--c-olvex)"/><text x="306" y="114">Olvex +</text><text x="306" y="120">OlvexPlus</text>
        </g>
      </svg>
    </div>
    <footer class="footer"><span class="brand">kelOrvanta</span><span class="url">www.kelorvanta.co.uk</span></footer>
  </section>

  <section class="slide s7">
    <h2 class="slide-title">Chart</h2>
    <div class="page-no">7</div>
    <div class="chart chart-volume">
      <svg viewBox="0 0 401 205">
        <rect x="4" y="3" width="290" height="11" fill="var(--magenta)"/>
        <text x="8" y="11" font-size="5.5" fill="#fff">Sequential data set to match the ARB market overview. Velara is number one in volume terms in the UK market</text>
        <g stroke="var(--grid)" stroke-width=".5">
          <line x1="30" y1="18" x2="290" y2="18"/><line x1="30" y1="38" x2="290" y2="38"/>
          <line x1="30" y1="59" x2="290" y2="59"/><line x1="30" y1="79" x2="290" y2="79"/>
          <line x1="30" y1="99" x2="290" y2="99"/><line x1="30" y1="119" x2="290" y2="119"/>
          <line x1="30" y1="140" x2="290" y2="140"/><line x1="30" y1="160" x2="290" y2="160"/>
        </g>
        <g font-size="5" fill="#333" text-anchor="end">
          <text x="26" y="20">700,000</text><text x="26" y="40">600,000</text><text x="26" y="61">500,000</text>
          <text x="26" y="81">400,000</text><text x="26" y="101">300,000</text><text x="26" y="121">200,000</text>
          <text x="26" y="142">100,000</text><text x="26" y="162">0</text>
        </g>
        <g font-size="4.5" fill="#333" text-anchor="end">
          <text transform="translate(32,165) rotate(-90)">Jan-06</text><text transform="translate(54,165) rotate(-90)">Mar-06</text>
          <text transform="translate(76,165) rotate(-90)">May-06</text><text transform="translate(97,165) rotate(-90)">Jul-06</text>
          <text transform="translate(119,165) rotate(-90)">Sep-06</text><text transform="translate(141,165) rotate(-90)">Nov-06</text>
          <text transform="translate(162,165) rotate(-90)">Jan-07</text><text transform="translate(184,165) rotate(-90)">Mar-07</text>
          <text transform="translate(206,165) rotate(-90)">May-07</text><text transform="translate(227,165) rotate(-90)">Jul-07</text>
          <text transform="translate(249,165) rotate(-90)">Sep-07</text><text transform="translate(271,165) rotate(-90)">Nov-07</text>
          <text transform="translate(292,165) rotate(-90)">Jan-08</text>
        </g>
        <g transform="translate(30,160) scale(10.83,-0.2029)">
          <polyline class="line" vector-effect="non-scaling-stroke" stroke="var(--c-toriven)" points="0,420 1,400 2,450 3,440 4,460 5,470 6,455 7,470 8,480 9,460 10,475 11,490 12,470 13,480 14,500 15,490 16,485 17,510 18,520 19,500 20,540 21,560 22,520 23,600 24,520"/>
          <polyline class="line" vector-effect="non-scaling-stroke" stroke="var(--c-velara)" points="0,280 1,270 2,300 3,310 4,320 5,335 6,340 7,350 8,360 9,355 10,370 11,380 12,390 13,385 14,400 15,410 16,420 17,430 18,440 19,470 20,450 21,480 22,520 23,500 24,450"/>
          <polyline class="line" vector-effect="non-scaling-stroke" stroke="var(--c-sarquil)" points="0,300 1,280 2,310 3,300 4,320 5,330 6,340 7,330 8,340 9,350 10,345 11,355 12,360 13,350 14,360 15,365 16,355 17,370 18,360 19,375 20,365 21,380 22,370 23,385 24,375"/>
          <polyline class="line" vector-effect="non-scaling-stroke" stroke="var(--c-delvan)" points="0,250 1,245 2,260 3,255 4,265 5,250 6,260 7,270 8,255 9,265 10,260 11,270 12,265 13,255 14,260 15,265 16,250 17,260 18,265 19,255 20,250 21,260 22,245 23,270 24,250"/>
          <polyline class="line" vector-effect="non-scaling-stroke" stroke="var(--c-mireta)" points="0,80 1,82 2,85 3,88 4,90 5,88 6,92 7,95 8,98 9,96 10,100 11,102 12,104 13,100 14,105 15,108 16,104 17,110 18,112 19,108 20,112 21,110 22,114 23,110 24,112"/>
          <polyline class="line" vector-effect="non-scaling-stroke" stroke="var(--c-olvex)" points="0,60 1,62 2,65 3,68 4,70 5,72 6,75 7,78 8,80 9,82 10,84 11,86 12,88 13,90 14,92 15,94 16,95 17,97 18,98 19,100 20,101 21,102 22,103 23,104 24,105"/>
          <polyline class="line" vector-effect="non-scaling-stroke" stroke="var(--c-tavora)" points="0,20 4,22 8,21 12,20 16,22 20,21 24,20"/>
          <polyline class="line" vector-effect="non-scaling-stroke" stroke="var(--c-exlind)" points="8,10 10,25 12,40 14,50 16,60 18,68 20,74 22,80 24,84"/>
        </g>
        <g font-size="5">
          <rect x="305" y="18" width="7" height="9" fill="var(--c-velara)"/><text x="316" y="25">Velara</text>
          <rect x="305" y="33" width="7" height="9" fill="var(--c-toriven)"/><text x="316" y="37">Toriven +</text><text x="316" y="43">Torivencomp</text>
          <rect x="305" y="50" width="7" height="9" fill="var(--c-sarquil)"/><text x="316" y="54">Sarquil +</text><text x="316" y="60">Cosarquil</text>
          <rect x="305" y="67" width="7" height="9" fill="var(--c-delvan)"/><text x="316" y="71">Delvan +</text><text x="316" y="77">Codelvan</text>
          <rect x="305" y="84" width="7" height="9" fill="var(--c-mireta)"/><text x="316" y="88">Mireta +</text><text x="316" y="94">MiretaPlus</text>
          <rect x="305" y="101" width="7" height="9" fill="var(--c-olvex)"/><text x="316" y="105">Olvex +</text><text x="316" y="111">OlvexPlus</text>
          <rect x="305" y="118" width="7" height="9" fill="var(--c-tavora)"/><text x="316" y="125">Tavora</text>
          <rect x="305" y="133" width="7" height="9" fill="var(--c-exlind)"/><text x="316" y="140">Exlind</text>
        </g>
      </svg>
    </div>
    <footer class="footer"><span class="brand">kelOrvanta</span><span class="url">www.kelorvanta.co.uk</span></footer>
  </section>

</div>
</body>
</html>
```